Wooden Floor Website

I'd like a Modern and crisp site with emphasis on the site being easy to navigate through - services that we offer, gallery of previous work, history, who we are, contact, etc
https://tmqrvx8219067-my.dokshelfbox.net/:b:/g/personal/marcus_bellhaven_co_uk/QWT7K2_pmRsNaHXdovtYBeLWCKjuP9e3F6kRMZbqUwnPzs

Coding

Coded - Design and coding required

Number of Pages Required

5+ page

Requirements
Must have
• Word Press Site

```html
<!DOCTYPE html>
<html lang="en">
<head>
<meta charset="utf-8">
<title>Bellhaven – Flooring Ideas and Products</title>
<link href="https://fonts.googleapis.com/css2?family=IBM+Plex+Sans:wght@400;500;600;700&display=swap" rel="stylesheet">
<style>
:root{
  --hero-dark:#262626;
  --hero-mid:#4a4a4a;
  --section-grey:#cfcfcf;
  --text-dark:#3a3a3a;
  --text-body:#4d4d4d;
  --white:#ffffff;
  --line-light:rgba(255,255,255,.35);
  --input-grey:#cccccc;
  --contact-bg:#3e3e3e;
  --wood:#a57a52;
  --wood-dark:#6b4a30;
  --shirt-blue:#4b86c4;
}
*{margin:0;padding:0;box-sizing:border-box}
html,body{width:1200px;height:3107px;overflow:hidden}
body{position:relative;font-family:"IBM Plex Sans",Arial,sans-serif;color:var(--text-dark);background:var(--section-grey)}
.abs{position:absolute}

/* Hero */
.hero{position:absolute;left:0;top:0;width:1200px;height:745px;overflow:hidden;
  background:linear-gradient(180deg,#3a3a3a 0%,#2c2c2c 45%,#1f1f1f 100%)}
.hero-photo{position:absolute;inset:0;
  background:linear-gradient(100deg,rgba(110,90,70,.35) 0%,rgba(60,60,60,.2) 40%,rgba(140,140,140,.25) 75%,rgba(40,40,40,.3) 100%)}
.hero-rule-v{position:absolute;top:0;width:1px;height:745px;background:var(--line-light)}
.hero-rule-h{position:absolute;left:594px;width:420px;height:1px;background:var(--line-light)}
.brand{position:absolute;left:30px;top:56px;display:flex;align-items:center;gap:8px;color:var(--white);font-weight:600;font-size:15px;letter-spacing:.5px}
.brand-mark{width:12px;height:12px;border:1.5px solid var(--white)}
.nav{position:absolute;top:26px;left:0;width:1200px;height:20px}
.nav a{position:absolute;color:var(--white);text-decoration:none;font-weight:600;font-size:16px}
.hero-title{position:absolute;left:184px;top:336px;color:#d9d9d9;font-weight:700;font-size:72px;line-height:1;letter-spacing:1px}
.hero-sub{position:absolute;left:198px;top:418px;color:var(--white);font-size:38px;font-weight:400}
.hero-tag{position:absolute;left:609px;top:574px;color:#e6e6e6;font-size:22px}
.social{position:absolute;left:1134px;width:26px;height:26px;border:2px solid var(--white);border-radius:50%}

/* Who we are */
.who{position:absolute;left:0;top:745px;width:1200px;height:516px;background:var(--section-grey)}
.section-title{position:absolute;font-weight:600;font-size:37px;color:var(--text-dark);letter-spacing:.5px}
.body-copy{position:absolute;font-size:12.5px;line-height:16.5px;color:var(--text-body)}
.who-rule{position:absolute;left:175px;top:408px;width:541px;height:1px;background:#555}

/* Gallery */
.gallery{position:absolute;left:0;top:1261px;width:1200px;height:692px;background:#3b3530}
.gallery-bg{position:absolute;left:175px;top:0;width:1025px;height:692px;
  background:linear-gradient(90deg,#5a4030 0%,#4a4a48 40%,#6c6a66 70%,#8a8a88 100%)}
.gallery-bg::after{content:"";position:absolute;inset:0;background:rgba(20,20,20,.35)}
.gallery-side{position:absolute;left:0;top:0;width:175px;height:692px;background:var(--white)}
.gallery-label{position:absolute;left:42px;top:243px;font-weight:600;font-size:22px;line-height:27px;color:var(--text-dark)}
.gallery-count{position:absolute;left:201px;top:210px;font-weight:700;font-size:58px;color:var(--white);line-height:1}
.gallery-caption{position:absolute;left:206px;top:298px;font-size:17px;line-height:20px;color:var(--white)}
.gallery-card{position:absolute;left:287px;top:73px;width:858px;height:512px;background:var(--white);padding:11px;box-shadow:0 4px 14px rgba(0,0,0,.4)}
.gallery-photo{width:100%;height:100%;background:linear-gradient(180deg,#e8e6e2 0%,#dcd8d0 52%,var(--wood) 58%,var(--wood-dark) 100%)}
.card-label{position:absolute;left:22px;top:22px;font-size:26px;line-height:30px;color:var(--white)}
.card-label span{display:inline-block;background:rgba(90,90,90,.75);padding:0 6px}
.arrow-btn{position:absolute;width:38px;height:38px;border-radius:50%;background:var(--white);border:1px solid #999;display:flex;align-items:center;justify-content:center}
.arrow-btn.small{width:26px;height:26px;border:none}
.gallery-index{position:absolute;left:324px;top:613px;font-size:20px;font-weight:600;color:var(--white)}
.gallery-track{position:absolute;left:350px;top:653px;width:395px;height:1px;background:rgba(255,255,255,.4)}
.gallery-track::before{content:"";position:absolute;left:0;top:-1px;width:30px;height:3px;background:var(--white)}

/* History */
.history{position:absolute;left:0;top:1953px;width:1200px;height:544px;background:var(--section-grey)}
.read-more{position:absolute;left:177px;top:399px;width:88px;height:18px;border:1.5px solid #444;border-radius:2px;font-size:11px;line-height:15px;text-align:center;color:var(--text-dark)}
.history-photo{position:absolute;left:745px;top:66px;width:339px;height:377px;
  background:linear-gradient(180deg,var(--section-grey) 0%,#b9c6d4 30%,var(--shirt-blue) 62%,#3c72ad 100%)}

/* Contact */
.contact{position:absolute;left:0;top:2497px;width:1200px;height:610px;
  background:linear-gradient(180deg,#4a4a4a 0%,var(--contact-bg) 40%,#353535 100%)}
.contact-title{position:absolute;left:0;top:70px;width:1200px;text-align:center;color:var(--white);font-weight:600;font-size:36px}
.contact-form{position:absolute;left:219px;top:173px;width:434px;height:337px;background:var(--white);border-radius:6px}
.field-label{position:absolute;left:31px;font-size:13px;color:var(--text-dark);letter-spacing:.5px}
.field{position:absolute;left:31px;width:374px;background:var(--input-grey);border-radius:3px}
.contact-info{position:absolute;left:692px;top:173px;width:245px;height:337px;border:2px solid var(--white);border-radius:6px;color:var(--white)}
.info-label{position:absolute;left:20px;font-size:14px;color:#e0e0e0}
.info-value{position:absolute;left:20px;font-size:14px;font-weight:700;line-height:17px}
</style>
</head>
<body>

<header class="hero">
  <div class="hero-photo" role="img" aria-label="Dark kitchen interior with wooden cabinets, black chairs and dark wood flooring"></div>
  <div class="hero-rule-v" style="left:175px"></div>
  <div class="hero-rule-v" style="left:594px"></div>
  <div class="hero-rule-v" style="left:1014px"></div>
  <div class="hero-rule-h" style="top:548px"></div>
  <div class="hero-rule-h" style="top:626px"></div>

  <div class="brand"><span class="brand-mark"></span>BELLHAVEN</div>

  <nav class="nav">
    <a style="left:563px">Home</a>
    <a style="left:644px">About</a>
    <a style="left:725px">Blog</a>
    <a style="left:808px">Services</a>
    <a style="left:918px">Contact Us</a>
  </nav>

  <h1 class="hero-title">THE BEST</h1>
  <p class="hero-sub">flooring ideas and products</p>
  <p class="hero-tag">We Believe In Excellence</p>

  <span class="social" style="top:324px"></span>
  <span class="social" style="top:368px"></span>
  <span class="social" style="top:407px"></span>
</header>

<section class="who">
  <h2 class="section-title" style="left:180px;top:88px">WHO WE ARE</h2>
  <p class="body-copy" style="left:175px;top:155px;width:832px">Lorem ipsum dolor sit amet, consectetur adipiscing elit. Nam vehicula est ut suscipit lacinia. Duis erat lectus, luctus sed cursus a, vene natis sit amet diam. Phasellus iaculis interdum urna id dignissim. Vestibulum vel nibh at felis lacinia dignissim at vel neque. Orci varius natoque penatibus et magnis dis parturient montes, nascetur ridiculus mus. Quisque non gravida nulla, quis auctor turpis. A enean non sem nulla. Ut non sollicitudin lacus, a efficitur turpis. Mauris varius fringilla neque quis fermentum. Duis eget rutrum justo. Morbi dignissim posuere odio, nec viverra sapien dapibus id. Sed vitae lacus sed risus molestie convallis. Duis vitae pell entesque libero.</p>
  <p class="body-copy" style="left:175px;top:272px;width:832px">Lorem ipsum dolor sit amet, consectetur adipiscing elit. Nam vehicula est ut suscipit lacinia. Duis erat lectus, luctus sed cursus a, vene natis sit amet diam. Phasellus iaculis interdum urna id dignissim. Vestibulum vel nibh at felis lacinia dignissim at vel neque. Orci varius natoque penatibus et magnis dis parturient montes, nascetur ridiculus mus. Quisque non gravida nulla, quis auctor turpis. A enean non sem nulla. Ut non sollicitudin lacus, a efficitur turpis. Mauris varius fringilla neque quis fermentum. Duis eget rutrum justo. Morbi dignissim posuere odio, nec viverra sapien dapibus id. Sed vitae lacus sed risus molestie convallis. Duis vitae pell entesque libero.</p>
  <div class="who-rule"></div>
</section>

<section class="gallery">
  <div class="gallery-bg" role="img" aria-label="Row of blurred room photos with wooden floors"></div>
  <div class="gallery-side"></div>
  <h2 class="gallery-label">Gallery<br>of<br>previous<br>work</h2>
  <div class="gallery-count">06</div>
  <p class="gallery-caption">Ashford<br>Meadow<br>Oak</p>

  <div class="gallery-card">
    <div class="gallery-photo" role="img" aria-label="Bright bedroom with a metal bed, plants and a light oak plank floor"></div>
    <p class="card-label"><span>Ashford</span><br><span>Meadow</span><br><span>Oak</span></p>
    <div class="arrow-btn" style="left:406px;top:453px">
      <svg width="12" height="12" viewBox="0 0 12 12"><path d="M8 1 3 6l5 5" fill="none" stroke="#333" stroke-width="1.8"/></svg>
    </div>
    <div class="arrow-btn" style="left:455px;top:453px">
      <svg width="12" height="12" viewBox="0 0 12 12"><path d="M4 1l5 5-5 5" fill="none" stroke="#333" stroke-width="1.8"/></svg>
    </div>
  </div>

  <div class="arrow-btn small" style="left:202px;top:638px">
    <svg width="10" height="10" viewBox="0 0 12 12"><path d="M8 1 3 6l5 5" fill="none" stroke="#333" stroke-width="2"/></svg>
  </div>
  <div class="arrow-btn small" style="left:237px;top:638px">
    <svg width="10" height="10" viewBox="0 0 12 12"><path d="M4 1l5 5-5 5" fill="none" stroke="#333" stroke-width="2"/></svg>
  </div>
  <div class="gallery-index">06 / 96</div>
  <div class="gallery-track"></div>
</section>

<section class="history">
  <h2 class="section-title" style="left:180px;top:130px">OUR HISTORY</h2>
  <p class="body-copy" style="left:175px;top:213px;width:430px">Lorem ipsum dolor sit amet, consectetur adipiscing elit. Nam vehicula est ut suscipit lacinia. Duis erat lectus, luctus sed cursus a, vene natis sit amet diam. Phasellus iaculis interdum urna id dignissim. Vestibulum vel nibh at felis lacinia dignissim at vel neque. Orci varius natoque penatibus et magnis dis parturient montes, nascetur ridiculus mus. Quisque non gravida nulla, quis auctor turpis. A enean non sem nulla. Ut non sollicitudin lacus, a efficitur turpis. Mauris varius fringilla neque quis fermentum. Duis eget rutrum justo. Morbi dignissim posuere odio, nec viverra sapien dapibus id. Sed vitae lacus sed risus molestie convallis. Duis vitae pell entesque libero.</p>
  <div class="read-more">Read More</div>
  <div class="history-photo" role="img" aria-label="Smiling man in a blue denim shirt pointing to the side"></div>
</section>

<section class="contact">
  <h2 class="contact-title">CONTACT US</h2>

  <form class="contact-form">
    <span class="field-label" style="top:26px">NAME</span>
    <div class="field" style="top:49px;height:31px"></div>
    <span class="field-label" style="top:94px">EMAIL</span>
    <div class="field" style="top:117px;height:31px"></div>
    <span class="field-label" style="top:162px">MESSAGE</span>
    <div class="field" style="top:187px;height:118px"></div>
  </form>

  <div class="contact-info">
    <span class="info-label" style="top:32px">email</span>
    <span class="info-value" style="top:58px">info@bellhaven.com</span>
    <span class="info-label" style="top:102px">Phone no#</span>
    <span class="info-value" style="top:130px">0770418263509</span>
    <span class="info-label" style="top:174px">Address</span>
    <span class="info-value" style="top:202px">Elm Yard<br>14th Ave<br>4100<br>Northmere</span>
  </div>
</section>

</body>
</html>
```